Company providing Business Management Services needs modern business card

The business provides services like tender preparation, bank submissions, business health checks, financial and admin support. We want to portray 'Trust', 'Strength' and 'Support'.
2 styles of logo in various formats have been uploaded.
Looking for easy to understand, yet sophisticated and stand out from the crowd.

Target Market(s)

Small and Medium sized businesses

Industry/Entity Type

Business

Contact Information for Business Card

Name - Daniel Vesterby, Description - Manager, Phone - 0472 915 603, Email - danielvesterby@kpwholdingsgroup.example, Work description - Business Management Services.

Requirements
Must have
• Logo

```html
<!DOCTYPE html>
<html lang="en">
<head>
<meta charset="utf-8">
<title>KPW Holdings Group – Business Card</title>
<link href="https://fonts.googleapis.com/css2?family=Cinzel:wght@700&family=Montserrat:wght@300;400;600&display=swap" rel="stylesheet">
<style>
  :root{
    --page:#e4e0da;
    --card:#0c0c0c;
    --card-edge:#1c1c1c;
    --white:#ffffff;
    --grey:#9a9a9a;
    --purple:#9b4fc4;
    --blue:#3f7fd6;
    --green:#5cbf45;
    --orange:#f0852a;
  }
  *{box-sizing:border-box;margin:0;padding:0}
  html,body{width:1200px;height:900px;overflow:hidden}
  body{background:var(--page);display:flex;align-items:center;justify-content:center;gap:60px}
  .card{position:relative;width:520px;height:318px;background:linear-gradient(135deg,var(--card-edge),var(--card) 55%);border-radius:4px;box-shadow:0 14px 34px rgba(0,0,0,.28);overflow:hidden;color:var(--white)}

  /* brand lockup */
  .brand{position:absolute;display:flex;align-items:center;gap:14px}
  .brand-square{background:var(--grey);flex:none}
  .brand-name{font-family:"Montserrat",sans-serif;font-weight:600;color:var(--white);letter-spacing:.02em;line-height:1.1}

  /* front */
  .card--front .brand{top:38px;right:36px}
  .card--front .brand-square{width:40px;height:40px}
  .card--front .brand-name{font-size:22px}
  .contact{position:absolute;left:58px;bottom:40px}
  .contact-name{font-family:"Cinzel",serif;font-weight:700;font-size:22px;letter-spacing:.04em}
  .contact-role{font-family:"Cinzel",serif;font-weight:700;font-size:14px;color:var(--orange);letter-spacing:.06em;margin:2px 0 20px}
  .contact-line{font-family:"Montserrat",sans-serif;font-weight:300;display:flex;align-items:center;height:34px}
  .contact-phone{font-size:22px;letter-spacing:.04em}
  .contact-email{font-size:13px;letter-spacing:.03em}
  .tab{position:absolute;left:0;width:38px;height:30px;border-radius:0 8px 8px 0;display:flex;align-items:center;justify-content:center}
  .tab--phone{background:var(--purple);bottom:76px}
  .tab--mail{background:var(--green);bottom:42px}
  .tab svg{width:16px;height:16px}

  /* back */
  .card--back .services{position:absolute;left:40px;top:112px;font-family:"Cinzel",serif;font-weight:700;font-size:15px;color:var(--blue);letter-spacing:.05em}
  .edge-bars{position:absolute;left:34px;top:0;display:flex;gap:18px}
  .edge-bar{width:76px;height:20px;border-radius:0 0 3px 3px}
  .edge-bar--purple{background:var(--purple)}
  .edge-bar--blue{background:var(--blue)}
  .edge-bar--green{background:var(--green)}
  .edge-bar--orange{background:var(--orange)}
  .card--back .brand{right:40px;bottom:60px}
  .card--back .brand-square{width:56px;height:56px}
  .card--back .brand-name{font-size:30px}
</style>
</head>
<body>

<section class="card card--front" aria-label="Business card front">
  <div class="brand">
    <span class="brand-square"></span>
    <span class="brand-name">KPW Holdings<br>Group</span>
  </div>

  <span class="tab tab--phone">
    <svg viewBox="0 0 24 24" fill="#fff"><path d="M6.6 10.8a15.1 15.1 0 0 0 6.6 6.6l2.2-2.2a1 1 0 0 1 1-.25 11.4 11.4 0 0 0 3.6.57 1 1 0 0 1 1 1V20a1 1 0 0 1-1 1A17 17 0 0 1 3 4a1 1 0 0 1 1-1h3.5a1 1 0 0 1 1 1c0 1.25.2 2.45.57 3.6a1 1 0 0 1-.25 1z"/></svg>
  </span>
  <span class="tab tab--mail">
    <svg viewBox="0 0 24 24" fill="none" stroke="#fff" stroke-width="2"><rect x="3" y="5" width="18" height="14" rx="1"/><path d="M3 6l9 7 9-7"/></svg>
  </span>

  <div class="contact">
    <p class="contact-name">Daniel Vesterby</p>
    <p class="contact-role">Manager</p>
    <p class="contact-line contact-phone">0472 915 603</p>
    <p class="contact-line contact-email">danielvesterby@kpwholdingsgroup.example</p>
  </div>
</section>

<section class="card card--back" aria-label="Business card back">
  <div class="edge-bars">
    <span class="edge-bar edge-bar--purple"></span>
    <span class="edge-bar edge-bar--blue"></span>
    <span class="edge-bar edge-bar--green"></span>
    <span class="edge-bar edge-bar--orange"></span>
  </div>
  <p class="services">Business Management Services</p>
  <div class="brand">
    <span class="brand-square"></span>
    <span class="brand-name">KPW Holdings<br>Group</span>
  </div>
</section>

</body>
</html>
```